Chiropractic Business Card

I need a business card designed to help me stand apart from my competition. I really like simple, clean designs that appear open and inviting. I would like the designs to incorporate the color blue, green, or both. I really like the attached picture because it highlights that I just don't treat "back pain" and it being a nice computer graphic helps show that I have a modern practice. "Modern practice" meaning merging technology and most current research in my patient care.

My information is:

Wesley Harmon, DC
Phone- (707) 555-0182
Email- drwesleyharmon@mailbox-example.com
Website- www.fernleachiropractic-example.com
Address- 248 Pellham Street, Sonoma, CA 95400

Jpeg and pdf attached of Fernlea Chiropractic logo.
Updates

Atmosphere to be clean lines and solid colors to be have gradient fading, but don't want too much going on with the fading. Simple.

Target Market(s)

Active adults who are health conscious between the ages of 20-70

Industry/Entity Type

Computer

Colors
0455a3
85cae6

Requirements
Must have
• Change color of Fernlea chiropractic logo (maroon) to fit the rest of the design.
Nice to have
• Can separate the running image from the black background to have it work with the design.

```html
<!DOCTYPE html>
<html lang="en">
<head>
<meta charset="utf-8">
<title>Fernlea Chiropractic – Business Card</title>
<link href="https://fonts.googleapis.com/css2?family=Ubuntu:wght@400;500;700&display=swap" rel="stylesheet">
<style>
  :root {
    --page-bg: #2a2a2a;
    --card-white: #ffffff;
    --card-black: #0b0b0c;
    --brand-blue: #0455a3;
    --brand-sky: #85cae6;
    --band-maroon: #8c0f30;
    --text-grey: #5a5a5a;
    --text-light: #c9c9c9;
    --figure-light: #a9cce0;
    --figure-deep: #5f88a6;
  }
  * { box-sizing: border-box; margin: 0; padding: 0; }
  html, body { width: 1200px; height: 1000px; overflow: hidden; }
  body {
    background: var(--page-bg);
    font-family: "Ubuntu", sans-serif;
    position: relative;
  }
  .card {
    position: absolute;
    top: 350px;
    width: 520px;
    height: 300px;
    overflow: hidden;
    box-shadow: 0 10px 30px rgba(0,0,0,.45);
  }
  .card--front { left: 70px; background: var(--card-white); }
  .card--back { left: 610px; background: var(--card-black); }

  .runner-art {
    position: absolute;
    top: 0;
    right: 0;
    width: 240px;
    height: 300px;
    background: linear-gradient(160deg, var(--figure-light), var(--figure-deep));
    opacity: .85;
    -webkit-mask-image: linear-gradient(90deg, transparent, #000 40%);
            mask-image: linear-gradient(90deg, transparent, #000 40%);
  }

  .brand-name {
    position: absolute;
    font-weight: 700;
    line-height: 1.1;
    letter-spacing: .5px;
  }
  .card--front .brand-name { left: 56px; top: 40px; font-size: 26px; color: var(--brand-blue); }
  .card--back .brand-name { left: 40px; top: 96px; font-size: 28px; color: var(--brand-sky); }

  .name-band {
    position: absolute;
    left: 0;
    top: 118px;
    width: 100%;
    height: 62px;
    display: flex;
  }
  .name-band__edge { width: 22px; background: #111; }
  .name-band__fill {
    flex: 1;
    background: linear-gradient(90deg, var(--band-maroon) 70%, rgba(140,15,48,.6));
    position: relative;
  }
  .person-name {
    position: absolute;
    left: 36px;
    top: 10px;
    color: #fff;
    font-weight: 500;
    font-size: 17px;
  }
  .contact-direct {
    position: absolute;
    right: 18px;
    top: 14px;
    text-align: right;
    color: #fff;
    font-size: 12px;
    line-height: 1.5;
  }
  .contact-direct .phone { font-weight: 700; }

  .office-details {
    position: absolute;
    left: 58px;
    top: 200px;
    font-size: 12px;
    line-height: 1.45;
    color: var(--text-grey);
  }
  .office-details .office-name { color: var(--band-maroon); font-weight: 700; }

  .web-address {
    position: absolute;
    left: 42px;
    top: 190px;
    color: var(--text-light);
    font-size: 13px;
    letter-spacing: .4px;
  }
</style>
</head>
<body>

  <section class="card card--front" aria-label="Business card front">
    <div class="runner-art" role="img" aria-label="Translucent blue anatomical figure of a runner"></div>
    <div class="brand-name">FERNLEA<br>CHIROPRACTIC</div>
    <div class="name-band">
      <div class="name-band__edge"></div>
      <div class="name-band__fill">
        <p class="person-name">Wesley Harmon, DC</p>
        <p class="contact-direct">
          drwesleyharmon@mailbox-example.com<br>
          <span class="phone">(707) 555-0182</span> - Phone
        </p>
      </div>
    </div>
    <div class="office-details">
      <p class="office-name">FERNLEA CHIROPRACTIC OFFICES INC.</p>
      <p>248 Pellham Street, Sonoma, CA 95400</p>
      <p>www.fernleachiropractic-example.com</p>
    </div>
  </section>

  <section class="card card--back" aria-label="Business card back">
    <div class="runner-art" role="img" aria-label="Translucent blue anatomical figure of a runner"></div>
    <div class="brand-name">FERNLEA<br>CHIROPRACTIC</div>
    <p class="web-address">www.fernleachiropractic-example.com</p>
  </section>

</body>
</html>
```